Clean and modern business cards

Looking for an updated business card design for my dental office “tovrelle dental” . Looking for a modern clean / sleek design . I’m thinking black background but open to seeing other options . One side needs to have an appointment card . Card needs to have logo, dentist name , phone, email , address . I’ve attached couple of cards I thought were cool as well as my logo
Target Market(s)
Dental patients
Industry/Entity Type
Dentistry
Contact Information for Business Card
Phone email address

```html
<!DOCTYPE html>
<html lang="en">
<head>
<meta charset="utf-8">
<title>Tovrelle Dental – Business Cards</title>
<link href="https://fonts.googleapis.com/css2?family=Montserrat:wght@400;700&family=Arimo:wght@400;700&display=swap" rel="stylesheet">
<style>
  :root {
    --backdrop: #1d1d1f;
    --card-dark: #0b0b0b;
    --card-light: #f7f7f7;
    --accent-green: #9cc91a;
    --accent-gold: #e5b714;
    --text-light: #ffffff;
    --text-dark: #2a2a2a;
    --text-muted: #8a8a8a;
    --rule-light: #c9c9c9;
    --rule-dark: #4a4a4a;
  }
  * { box-sizing: border-box; margin: 0; padding: 0; }
  html, body { width: 1200px; height: 900px; overflow: hidden; }
  body {
    background: var(--backdrop);
    font-family: "Arimo", Arial, sans-serif;
    position: relative;
  }
  .card {
    position: absolute;
    top: 295px;
    width: 540px;
    height: 310px;
    border-radius: 22px;
    overflow: hidden;
  }
  .card-front { left: 40px; background: var(--card-dark); color: var(--text-light); }
  .card-back { left: 620px; background: var(--card-light); color: var(--text-dark); }
  .accent-stripe {
    position: absolute;
    left: 0; right: 0;
    bottom: 46px;
    height: 5px;
    background: var(--accent-green);
  }

  /* Front */
  .brand {
    position: absolute;
    left: 34px;
    top: 150px;
    display: flex;
    align-items: center;
    gap: 14px;
  }
  .brand-dot {
    width: 58px; height: 58px;
    border-radius: 50%;
    background: var(--accent-green);
  }
  .brand-name {
    font-family: "Montserrat", sans-serif;
    font-weight: 700;
    font-size: 24px;
    line-height: 1.05;
    letter-spacing: 0.5px;
    text-transform: uppercase;
    color: var(--text-light);
  }
  .divider {
    position: absolute;
    left: 268px;
    top: 70px;
    width: 1px;
    height: 170px;
    background: var(--rule-dark);
  }
  .contact {
    position: absolute;
    left: 290px;
    top: 70px;
  }
  .person-name {
    font-family: "Montserrat", sans-serif;
    font-weight: 700;
    font-size: 19px;
    color: var(--accent-gold);
    text-transform: uppercase;
    letter-spacing: 0.3px;
  }
  .person-role { font-size: 14px; margin-bottom: 14px; }
  .contact-list { list-style: none; }
  .contact-list li {
    display: flex;
    align-items: center;
    gap: 8px;
    font-size: 13.5px;
    line-height: 21px;
  }
  .contact-list svg { width: 13px; height: 13px; flex: none; }
  .highlight { color: var(--accent-gold); }
  .address { font-size: 13.5px; line-height: 19px; margin-top: 12px; }

  /* Back */
  .watermark {
    position: absolute;
    right: 40px;
    top: 18px;
    width: 230px;
    height: 230px;
    border-radius: 50%;
    background: radial-gradient(circle, rgba(190,210,235,0.35) 0%, rgba(230,220,240,0.25) 55%, rgba(247,247,247,0) 72%);
  }
  .appointment-title {
    position: absolute;
    top: 42px;
    left: 0; right: 0;
    text-align: center;
    font-size: 19px;
    font-weight: 400;
    letter-spacing: 0.3px;
  }
  .field {
    position: absolute;
    display: flex;
    align-items: flex-end;
    color: var(--text-muted);
    font-size: 16px;
  }
  .field-line {
    flex: 1;
    border-bottom: 1px solid var(--rule-light);
    margin-left: 8px;
    height: 18px;
  }
  .field-name { left: 40px; top: 104px; width: 230px; }
  .field-time { left: 290px; top: 104px; width: 210px; }
  .field-date { left: 40px; top: 150px; width: 460px; }
  .suffix { margin-left: 6px; }
  .policy-note {
    position: absolute;
    left: 0; right: 0;
    top: 204px;
    text-align: center;
    font-size: 13px;
    line-height: 18px;
    color: var(--text-dark);
  }
</style>
</head>
<body>

<section class="card card-front" aria-label="Business card front">
  <div class="brand">
    <span class="brand-dot"></span>
    <span class="brand-name">Tovrelle<br>Dental</span>
  </div>
  <div class="divider"></div>
  <div class="contact">
    <p class="person-name">Marcus Ellery</p>
    <p class="person-role">Managing Director</p>
    <ul class="contact-list">
      <li>
        <svg viewBox="0 0 24 24" aria-hidden="true"><path fill="#e5b714" d="M6.6 10.8a15 15 0 0 0 6.6 6.6l2.2-2.2c.3-.3.7-.4 1-.2 1.1.4 2.3.6 3.6.6.6 0 1 .4 1 1V20c0 .6-.4 1-1 1A17 17 0 0 1 3 4c0-.6.4-1 1-1h3.5c.6 0 1 .4 1 1 0 1.3.2 2.5.6 3.6.1.3 0 .7-.2 1z"/></svg>
        044-310 582 947
      </li>
      <li>
        <svg viewBox="0 0 24 24" aria-hidden="true"><rect x="2" y="5" width="20" height="14" fill="#e5b714"/><path d="M2 5l10 8 10-8" stroke="#0b0b0b" stroke-width="2" fill="none"/></svg>
        hello@tovrelle.com
      </li>
      <li>
        <svg viewBox="0 0 24 24" aria-hidden="true"><g fill="none" stroke="#e5b714" stroke-width="2"><circle cx="12" cy="12" r="10"/><ellipse cx="12" cy="12" rx="4" ry="10"/><path d="M2 12h20M4 7h16M4 17h16"/></g></svg>
        <span>www.<span class="highlight">tovrelledental</span>.com</span>
      </li>
    </ul>
    <p class="address">421, Address line goes here<br>45452, Country Name</p>
  </div>
  <div class="accent-stripe"></div>
</section>

<section class="card card-back" aria-label="Appointment card back">
  <div class="watermark" role="img" aria-label="Faint brand emblem decoration"></div>
  <h2 class="appointment-title">NEXT APPOINTMENT</h2>
  <div class="field field-name">Name<span class="field-line"></span></div>
  <div class="field field-time">Time<span class="field-line"></span><span class="suffix">am/pm</span></div>
  <div class="field field-date">Date<span class="field-line"></span></div>
  <p class="policy-note">To cancel or reschedule please notify us atleast<br>48 hours prior to your scheduled appointment</p>
  <div class="accent-stripe"></div>
</section>

</body>
</html>
```